Food broker, trader, wholesaler, liquidator looking for a 5 pages website

Looking for a 5 pages website design. We are food brokers, traders, wholesaler and closeout buyer working with manufacturers, distributors, importers sell to retailers, food service operators and industrial (ingredients). We help market their products. We are a resource for those who need a solution in the distribution/selling/placement of food on the shelves, kitchens and pantries. Whether we open new accounts with new products or sell short dated inventory, we know where to go and get results.

Target Market(s)

Food manufacturers, food distributors, food brokers

Coding

Coded - Design and coding required

Number of Pages Required

4 page

Font styles to use
Serif

Requirements
Must have
• Food-food production-warehouse-Food packaging-people meeting-trucks-supermarket shelves-

```html
<!DOCTYPE html>
<html lang="en">
<head>
<meta charset="utf-8">
<title>Larder & Co. — Food Brokers, Traders & Wholesalers</title>
<link href="https://fonts.googleapis.com/css2?family=Montserrat:wght@400;600;800;900&family=Raleway:wght@400;500;600;700&display=swap" rel="stylesheet">
<style>
:root{
  --navy:#0c1766;
  --navy-deep:#060b35;
  --royal:#1d33c9;
  --heading:#2a3aa0;
  --ink:#2b2b33;
  --muted:#6b6f80;
  --white:#ffffff;
  --paper:#f4f5f8;
  --accent-blue:#2f6bff;
}
*{box-sizing:border-box;margin:0;padding:0}
html,body{width:1200px;height:3748px;overflow:hidden}
body{font-family:"Raleway",sans-serif;color:var(--ink);background:var(--white);position:relative}
a{color:inherit;text-decoration:none}

/* ---------- Hero ---------- */
.hero{position:absolute;left:0;top:0;width:1200px;height:660px;overflow:hidden}
.hero-photo{position:absolute;inset:0;background:
  linear-gradient(180deg,rgba(10,16,60,.55) 0%,rgba(10,16,60,.25) 40%,rgba(10,16,60,.35) 100%),
  linear-gradient(115deg,#7a4a2a 0%,#b07a4c 30%,#2f6f6a 55%,#c49a66 80%,#8a5a35 100%)}
.topbar{position:absolute;top:0;left:0;right:0;height:30px;display:flex;justify-content:space-between;align-items:center;padding:0 112px;font-size:12px;color:var(--white);opacity:.9}
.topbar span{display:flex;align-items:center;gap:6px}
.nav{position:absolute;top:44px;left:112px;right:112px;height:56px;display:flex;justify-content:space-between;align-items:center}
.brand{display:flex;align-items:center;gap:10px;font-family:"Raleway",sans-serif;font-weight:700;font-size:15px;color:var(--white);letter-spacing:.5px}
.brand-dot{width:40px;height:40px;border-radius:50%;background:var(--navy)}
.menu{display:flex;gap:34px;font-size:15px;font-weight:600;color:var(--white)}
.menu a.active{border-bottom:2px solid var(--white);padding-bottom:4px}
.hero-copy{position:absolute;top:220px;left:0;right:0;text-align:center;color:var(--white)}
.hero-copy h1{font-family:"Raleway",sans-serif;font-weight:500;font-size:38px;letter-spacing:.2px}
.hero-copy p{margin-top:12px;font-size:17px;opacity:.9}
.hero-actions{margin-top:24px;display:flex;justify-content:center;gap:18px}
.btn{display:inline-block;height:38px;line-height:38px;padding:0 26px;border-radius:3px;font-size:14px;font-weight:600}
.btn-primary{background:var(--royal);color:var(--white)}
.btn-light{background:var(--white);color:var(--navy)}
.slider-dots{margin-top:30px;display:flex;justify-content:center;gap:8px}
.slider-dots i{width:10px;height:10px;border-radius:50%;background:rgba(255,255,255,.5)}
.slider-dots i.on{background:var(--white)}
.hero-edge{position:absolute;left:0;bottom:0;width:1200px;height:60px}

/* ---------- Intro ---------- */
.intro{position:absolute;top:660px;left:0;width:1200px;height:328px;text-align:center}
.intro-bg{position:absolute;right:120px;top:20px;width:420px;height:280px;border-radius:50%;background:radial-gradient(circle,rgba(230,200,150,.35),rgba(255,255,255,0) 70%)}
.intro h2{position:relative;margin-top:24px;font-weight:700;font-size:26px;color:var(--heading)}
.intro p{position:relative;width:720px;margin:18px auto 0;font-size:15px;line-height:22px;color:var(--ink)}
.intro .read-more{position:relative;display:inline-block;margin-top:40px;font-size:12px;font-weight:700;color:var(--heading);border-bottom:1px solid var(--heading)}

/* ---------- Feature photo ---------- */
.feature-photo{position:absolute;top:988px;left:0;width:1200px;height:524px;background:linear-gradient(100deg,#c9d6df 0%,#e9b380 35%,#6c9a3f 60%,#3b6a2a 80%,#a6843e 100%)}

/* ---------- What we do ---------- */
.services{position:absolute;top:1512px;left:0;width:1200px;height:848px;overflow:hidden}
.services-bg{position:absolute;inset:0;background:
  radial-gradient(ellipse 260px 400px at 0% 75%,#d9dfe6 0%,rgba(255,255,255,0) 100%),
  radial-gradient(ellipse 260px 400px at 100% 80%,#e3e5ea 0%,rgba(255,255,255,0) 100%),
  radial-gradient(ellipse 240px 220px at 100% 10%,#e2cfa6 0%,rgba(255,255,255,0) 100%),
  #f7f7f9}
.section-title{position:relative;text-align:center;font-family:"Montserrat",sans-serif;font-weight:600;font-size:24px;color:var(--heading);letter-spacing:.5px}
.services .section-title{margin-top:156px}
.title-rule{width:60px;height:2px;background:var(--heading);margin:10px auto 0}
.service-cards{position:absolute;top:216px;left:112px;width:976px;display:flex;justify-content:space-between}
.service-card{width:296px;height:264px;background:var(--white);box-shadow:0 6px 24px rgba(20,30,80,.12);text-align:center;padding:34px 28px 0}
.service-card svg{width:48px;height:48px}
.service-card h3{margin-top:18px;font-size:14px;font-weight:700;color:var(--ink)}
.service-card p{margin-top:10px;font-size:13px;line-height:19px;color:var(--muted)}
.services-note{position:absolute;top:584px;left:0;right:0;text-align:center;font-size:18px;line-height:27px;color:var(--ink)}
.services-welcome{position:absolute;top:724px;left:0;right:0;text-align:center;font-size:20px;font-weight:600;color:var(--heading)}

/* ---------- Featured products ---------- */
.products{position:absolute;top:2360px;left:0;width:1200px;height:496px;background:var(--white)}
.products .section-title{margin-top:0;font-family:"Montserrat",sans-serif;font-weight:800;font-size:26px;padding-top:0}
.product-grid{position:absolute;top:52px;left:112px;width:976px;display:flex;gap:4px}
.product-card{width:241px;height:440px;position:relative;background:var(--navy);overflow:hidden;color:var(--white);text-align:center}
.product-photo{height:176px}
.product-icon{position:absolute;top:146px;left:50%;margin-left:-30px;width:60px;height:60px;border-radius:50%;background:var(--white);display:flex;align-items:center;justify-content:center}
.product-card h3{margin-top:48px;font-family:"Montserrat",sans-serif;font-weight:900;font-size:26px;line-height:28px;letter-spacing:.5px}
.product-card p{margin:10px 22px 0;font-size:13px;line-height:18px;opacity:.9}
.product-base{position:absolute;left:0;bottom:0;width:241px;height:64px}

/* ---------- Testimonials ---------- */
.testimonials{position:absolute;top:2856px;left:0;width:1200px;height:444px;background:linear-gradient(180deg,#0e1a78 0%,var(--navy) 100%);color:var(--white);text-align:center}
.testimonials h2{margin-top:64px;font-family:"Raleway",sans-serif;font-weight:500;font-size:34px}
.avatars{margin-top:30px;display:flex;justify-content:center;align-items:center;gap:26px}
.avatar{border-radius:50%;background:linear-gradient(160deg,#9ea7c0,#5d6785)}
.avatar.sm{width:52px;height:52px;opacity:.7}
.avatar.lg{width:84px;height:84px;background:linear-gradient(160deg,#e7e9ef,#b7bccb)}
.avatars svg{width:18px;height:18px}
.quote{width:620px;margin:22px auto 0;font-size:15px;line-height:22px;color:#dde2ff}
.author{margin-top:56px;font-size:13px;color:#aab3e6}
.author::before{content:"";display:block;width:80px;height:1px;background:#5a66b8;margin:0 auto 10px}

/* ---------- Footer ---------- */
.footer{position:absolute;top:3300px;left:0;width:1200px;height:448px;background:var(--navy-deep);color:var(--white)}
.footer-cols{position:absolute;top:68px;left:112px;width:976px;display:flex}
.footer-about{width:260px}
.footer-about .brand{font-size:17px}
.footer-about .brand-dot{width:56px;height:56px;background:var(--royal)}
.footer-about p{margin-top:22px;font-size:13px;line-height:19px;color:#c6cbe8;width:200px}
.footer-col{width:240px}
.footer-col h4{font-family:"Montserrat",sans-serif;font-size:13px;font-weight:600;letter-spacing:1px;color:var(--accent-blue);margin-bottom:14px}
.footer-col li{list-style:none;font-size:13px;line-height:24px;color:#e3e6f7;display:flex;gap:8px;align-items:flex-start}
.footer-col li svg{width:14px;height:14px;margin-top:5px;flex:none}
.newsletter input{display:block;width:236px;height:36px;border:0;border-radius:2px;padding:0 12px;font-family:"Raleway",sans-serif;font-size:13px;color:var(--muted)}
.newsletter .btn{display:block;width:236px;margin-top:10px;height:34px;line-height:34px;background:var(--royal);color:var(--white);font-size:12px;text-align:center;border-radius:2px}
.socials{margin-top:14px;display:flex;gap:8px}
.socials i{width:30px;height:30px;border-radius:50%;background:var(--accent-blue)}
.copyright{position:absolute;top:352px;left:0;right:0;text-align:center;font-size:13px;color:#d8dcf0}
.copyright b{color:var(--accent-blue);font-weight:600}
</style>
</head>
<body>

<header class="hero">
  <div class="hero-photo" role="img" aria-label="Market stall with fresh bread loaves and produce crates"></div>
  <div class="topbar">
    <span><svg width="12" height="12" viewBox="0 0 24 24" fill="#fff"><path d="M6.6 10.8a15.1 15.1 0 0 0 6.6 6.6l2.2-2.2c.3-.3.7-.4 1-.2 1.1.4 2.3.6 3.6.6.6 0 1 .4 1 1V20c0 .6-.4 1-1 1A17 17 0 0 1 3 4c0-.6.4-1 1-1h3.5c.6 0 1 .4 1 1 0 1.3.2 2.5.6 3.6.1.3 0 .7-.2 1z"/></svg>Call us: (555) 014-2290</span>
    <span><svg width="12" height="12" viewBox="0 0 24 24" fill="#fff"><path d="M2 5h20v14H2zm2 2v.5l8 5 8-5V7z"/></svg>info@larderandco.com</span>
  </div>
  <nav class="nav">
    <div class="brand"><span class="brand-dot"></span>LARDER &amp; CO.</div>
    <div class="menu">
      <a class="active">Home</a><a>About US</a><a>What we do</a><a>Contact</a><a>Giving Back</a>
    </div>
  </nav>
  <div class="hero-copy">
    <h1>Larder &amp; Co. works with food manufacturers,</h1>
    <p>distributors, brokers and wholesalers to place their products</p>
    <div class="hero-actions"><a class="btn btn-primary">Read More</a><a class="btn btn-light">Free quote</a></div>
    <div class="slider-dots"><i class="on"></i><i></i><i></i></div>
  </div>
  <svg class="hero-edge" viewBox="0 0 1200 60" preserveAspectRatio="none"><path d="M0 30 L60 22 L120 34 L190 18 L260 30 L330 14 L400 28 L470 20 L540 36 L610 16 L690 30 L760 20 L840 34 L910 18 L990 30 L1060 22 L1130 34 L1200 24 L1200 60 L0 60Z" fill="#fff"/></svg>
</header>

<section class="intro">
  <div class="intro-bg"></div>
  <h2>Retail, Food Service and Industrial ingredients.</h2>
  <p>Retail, Food Service and Industrial ingredients.<br>
  Founded in 2008, Larder &amp; Co. started with the distribution of gluten free products un-<br>
  derstanding the need to provide access to unique flavors and products for the niche consum-<br>
  ers. From this we expanded into deli, dairy, groceries, frozen and beverages.</p>
  <a class="read-more">READ MORE</a>
</section>

<div class="feature-photo" role="img" aria-label="Child choosing fresh vegetables at a supermarket produce shelf"></div>

<section class="services">
  <div class="services-bg" role="img" aria-label="Soft kitchen backdrop with cheese, eggs, flour and wheat"></div>
  <h2 class="section-title">WHAT WE DO</h2>
  <div class="title-rule"></div>
  <div class="service-cards">
    <article class="service-card">
      <svg viewBox="0 0 48 48" fill="none" stroke="#1b1b22" stroke-width="2.5"><rect x="8" y="10" width="32" height="22"/><path d="M14 26l7-7 5 4 8-9M24 32v8M16 40h16"/></svg>
      <h3>Sales &amp; Marketing</h3>
      <p>we connect food buyers and sellers through a dedicated approach.</p>
    </article>
    <article class="service-card">
      <svg viewBox="0 0 48 48" fill="none" stroke="#1b1b22" stroke-width="2.5"><path d="M8 30l8-6h10l6 4M8 38l6-4h14l12-8"/><circle cx="30" cy="14" r="6"/></svg>
      <h3>Trading</h3>
      <p>we connect food buyers and sellers through a dedicated approach.</p>
    </article>
    <article class="service-card">
      <svg viewBox="0 0 48 48" fill="none" stroke="#1b1b22" stroke-width="2.5"><path d="M6 20L24 8l18 12v20H6z"/><rect x="16" y="24" width="16" height="16"/><path d="M16 30h16M16 35h16"/></svg>
      <h3>Closeout/Excess Inventory</h3>
      <p>we connect food buyers and sellers through a dedicated approach.</p>
    </article>
  </div>
  <p class="services-note">We pride ourselves in working in an easy, personal and accessible<br>
  environment making our customers and vendors comfortable with us.<br>
  We look forward to connecting with you and evaluating how we can assist<br>
  you reaching your sales objectives.</p>
  <p class="services-welcome">Welcome and thank you for visiting larderandco.com</p>
</section>

<section class="products">
  <h2 class="section-title">FEATURED PRODUCTS</h2>
  <div class="product-grid">
    <article class="product-card">
      <div class="product-photo" role="img" aria-label="Deli sandwich with cured meats" style="background:linear-gradient(160deg,#c98d58,#7c4a2a)"></div>
      <div class="product-icon"><svg width="30" height="30" viewBox="0 0 24 24" fill="none" stroke="#0c1766" stroke-width="2"><path d="M3 14h18M5 14c0-4 3-7 7-7s7 3 7 7M4 18h16"/></svg></div>
      <h3>DELI</h3>
      <p>Founded in 2008, Larder &amp; Co. started with the distribution</p>
      <svg class="product-base" viewBox="0 0 241 64" preserveAspectRatio="none"><path d="M0 20 L30 12 L70 22 L110 10 L150 20 L190 8 L241 18 L241 64 L0 64Z" fill="#1d33c9"/></svg>
    </article>
    <article class="product-card">
      <div class="product-photo" role="img" aria-label="Bowls of cheese, milk and eggs" style="background:linear-gradient(160deg,#e6dccb,#9a7a55)"></div>
      <div class="product-icon"><svg width="30" height="30" viewBox="0 0 24 24" fill="none" stroke="#0c1766" stroke-width="2"><path d="M8 3h8M9 3v4l-3 4v10h12V11l-3-4V3"/></svg></div>
      <h3>DAIRY</h3>
      <p>Founded in 2008, Larder &amp; Co. started with the distribution</p>
      <svg class="product-base" viewBox="0 0 241 64" preserveAspectRatio="none"><path d="M0 16 L40 24 L80 10 L120 22 L160 12 L200 24 L241 14 L241 64 L0 64Z" fill="#1d33c9"/></svg>
    </article>
    <article class="product-card">
      <div class="product-photo" role="img" aria-label="Grocery basket with packaged goods" style="background:linear-gradient(160deg,#4a5fbf,#1d2c7a)"></div>
      <div class="product-icon"><svg width="30" height="30" viewBox="0 0 24 24" fill="none" stroke="#0c1766" stroke-width="2"><path d="M3 5h3l2 11h11l2-8H7"/><circle cx="10" cy="20" r="1.5"/><circle cx="17" cy="20" r="1.5"/></svg></div>
      <h3>GROCERIES</h3>
      <p>Founded in 2008, Larder &amp; Co. started with the distribution</p>
      <svg class="product-base" viewBox="0 0 241 64" preserveAspectRatio="none"><path d="M0 22 L36 10 L76 20 L116 8 L156 22 L196 12 L241 20 L241 64 L0 64Z" fill="#1d33c9"/></svg>
    </article>
    <article class="product-card">
      <div class="product-photo" role="img" aria-label="Colourful chilled drinks in glasses" style="background:linear-gradient(160deg,#f07a4a,#c33a5a)"></div>
      <div class="product-icon"><svg width="30" height="30" viewBox="0 0 24 24" fill="none" stroke="#0c1766" stroke-width="2"><path d="M5 4h14l-6 8v7h3M13 19H8M13 12V19"/></svg></div>
      <h3>FROZEN AND<br>BEVERAGES</h3>
      <p>Founded in 2008, Larder &amp; Co. started with the distribution</p>
      <svg class="product-base" viewBox="0 0 241 64" preserveAspectRatio="none"><path d="M0 14 L44 22 L84 12 L124 24 L164 10 L204 20 L241 12 L241 64 L0 64Z" fill="#1d33c9"/></svg>
    </article>
  </div>
</section>

<section class="testimonials">
  <h2>People Say</h2>
  <div class="avatars">
    <svg viewBox="0 0 24 24" fill="#fff"><path d="M16 4L8 12l8 8z"/></svg>
    <div class="avatar sm" role="img" aria-label="Client portrait"></div>
    <div class="avatar lg" role="img" aria-label="Featured client portrait"></div>
    <div class="avatar sm" role="img" aria-label="Client portrait"></div>
    <svg viewBox="0 0 24 24" fill="#fff"><path d="M8 4l8 8-8 8z"/></svg>
  </div>
  <p class="quote">Lorem ipsum is simply dummy text of the printing and typesetting industry. Lorem Ipsum has been the industry's standard dummy text ever since the 1500s, when an unknown printer took a galley of type and scrambled it to make a type specimen book.</p>
  <p class="author">Dana Whitfield</p>
</section>

<footer class="footer">
  <div class="footer-cols">
    <div class="footer-about">
      <div class="brand"><span class="brand-dot"></span>LARDER &amp; CO.</div>
      <p>Lorem ipsum is simply dummy text of the printing and typesetting industry.</p>
    </div>
    <div class="footer-col">
      <h4>QUICK LINKS</h4>
      <ul><li>Home</li><li>About us</li><li>What we do</li><li>Contact</li><li>Giving Back</li></ul>
    </div>
    <div class="footer-col">
      <h4>REACH US</h4>
      <ul>
        <li><svg viewBox="0 0 24 24" fill="#2f6bff"><path d="M12 2a7 7 0 0 0-7 7c0 5 7 13 7 13s7-8 7-13a7 7 0 0 0-7-7zm0 9.5A2.5 2.5 0 1 1 12 6.5a2.5 2.5 0 0 1 0 5z"/></svg>48 Orchard Row, Unit 5<br>Fairview, NJ 07000</li>
        <li><svg viewBox="0 0 24 24" fill="#2f6bff"><path d="M6.6 10.8a15.1 15.1 0 0 0 6.6 6.6l2.2-2.2c.3-.3.7-.4 1-.2 1.1.4 2.3.6 3.6.6.6 0 1 .4 1 1V20c0 .6-.4 1-1 1A17 17 0 0 1 3 4c0-.6.4-1 1-1h3.5c.6 0 1 .4 1 1 0 1.3.2 2.5.6 3.6.1.3 0 .7-.2 1z"/></svg>(555) 014-2290</li>
        <li><svg viewBox="0 0 24 24" fill="#2f6bff"><path d="M2 5h20v14H2zm2 2v.5l8 5 8-5V7z"/></svg>info@larderandco.com</li>
      </ul>
    </div>
    <div class="footer-col newsletter">
      <h4>NEWSLETTER SIGNUP</h4>
      <input type="text" value="Enter your email">
      <a class="btn">NEWSLETTER SUBSCRIBE</a>
      <div class="socials"><i></i><i></i><i></i><i></i></div>
    </div>
  </div>
  <p class="copyright">Copyright © 2020 <b>Larder &amp; Co.</b></p>
</footer>

</body>
</html>
```